Steelcrest Process Systems. Needs a Business Card Design

We need a business card design for an engineering company which supplies industrial components (pumps, compressors, mechanical seals) provides repairs and services for above mentioned equipments. We offer a uniqe engineering solutions which help our customers to increase the productivness of their manufacturings, and energy savings.

Target Market(s)

Chemical and energy plants, refineries. Food industry and private consumers in a less.

Industry/Entity Type

Business

Contact Information for Business Card

Stylish and sleek design oriented on industrial area.

Requirements
Should not have
• company name shortening

```html
<!DOCTYPE html>
<html lang="en">
<head>
<meta charset="UTF-8">
<title>Steelcrest Process Systems – Business Cards</title>
<link rel="stylesheet" href="https://fonts.googleapis.com/css2?family=Nunito:wght@400;600;800&display=swap">
<style>
  :root {
    --backdrop: #d5d8d3;
    --card: #ffffff;
    --navy: #1d3a6e;
    --red: #e23a3c;
    --orange: #ef9a2a;
    --card-shadow: rgba(60, 66, 60, 0.22);
  }
  * { box-sizing: border-box; margin: 0; padding: 0; }
  html, body {
    width: 1200px;
    height: 1000px;
    overflow: hidden;
    background: var(--backdrop);
    font-family: "Nunito", sans-serif;
  }
  .stage { position: relative; width: 1200px; height: 1000px; }
  .card {
    position: absolute;
    width: 560px;
    height: 320px;
    background: var(--card);
    border-radius: 42px;
    box-shadow: 0 14px 30px var(--card-shadow);
  }
  .card--back { left: 500px; top: 140px; }
  .card--front { left: 150px; top: 500px; }

  .brand {
    position: absolute;
    display: flex;
    flex-direction: column;
    align-items: center;
    gap: 16px;
  }
  .card--back .brand { left: 0; right: 0; top: 78px; }
  .brand-dot {
    width: 84px;
    height: 84px;
    border-radius: 50%;
    background: var(--navy);
  }
  .brand-name {
    font-weight: 800;
    font-size: 30px;
    color: var(--navy);
    letter-spacing: 0.2px;
  }

  .front-mark {
    position: absolute;
    left: 52px;
    top: 70px;
    width: 200px;
    display: flex;
    flex-direction: column;
    align-items: center;
    gap: 14px;
  }
  .front-mark .brand-dot { width: 150px; height: 150px; }
  .front-mark .brand-name { font-size: 15px; text-align: center; }

  .details {
    position: absolute;
    right: 46px;
    top: 52px;
    text-align: right;
    color: var(--navy);
  }
  .details .company { font-weight: 800; font-size: 20px; }
  .details .person { font-weight: 800; font-size: 23px; }
  .details .role { font-weight: 800; font-size: 23px; margin-bottom: 12px; }

  .contacts { list-style: none; display: flex; flex-direction: column; gap: 3px; }
  .contacts li {
    display: flex;
    justify-content: flex-end;
    align-items: flex-start;
    gap: 8px;
    font-size: 16px;
    line-height: 1.15;
  }
  .contacts .icon { width: 15px; height: 15px; flex: none; margin-top: 2px; }
  .contacts .phone, .contacts .email { color: var(--red); }
  .contacts .web, .contacts .address { color: var(--orange); }
</style>
</head>
<body>
<main class="stage">
  <section class="card card--back" aria-label="Card back">
    <div class="brand">
      <span class="brand-dot"></span>
      <span class="brand-name">Steelcrest Process Systems</span>
    </div>
  </section>

  <section class="card card--front" aria-label="Card front">
    <div class="front-mark">
      <span class="brand-dot"></span>
      <span class="brand-name">Steelcrest Process Systems</span>
    </div>

    <div class="details">
      <p class="company">Steelcrest Process Systems</p>
      <p class="person">Name Surname</p>
      <p class="role">Your Title</p>
      <ul class="contacts">
        <li class="phone">
          <svg class="icon" viewBox="0 0 16 16" aria-hidden="true"><path fill="currentColor" d="M2 5c0-2 3-3 6-3s6 1 6 3v1h-3V4.8C10 4.3 9 4 8 4s-2 .3-3 .8V6H2zM4 7h8l2 6H2z"/></svg>
          <span>01 2345 6789</span>
        </li>
        <li class="email">
          <svg class="icon" viewBox="0 0 16 16" aria-hidden="true"><text x="8" y="13" text-anchor="middle" font-size="15" font-weight="700" fill="currentColor" font-family="Nunito, sans-serif">@</text></svg>
          <span>email@yourmail.com</span>
        </li>
        <li class="web">
          <svg class="icon" viewBox="0 0 16 16" aria-hidden="true"><g fill="none" stroke="currentColor" stroke-width="1.4"><circle cx="8" cy="8" r="6.3"/><ellipse cx="8" cy="8" rx="2.8" ry="6.3"/><path d="M1.7 8h12.6"/></g></svg>
          <span>www.yourweb.com</span>
        </li>
        <li class="address">
          <svg class="icon" viewBox="0 0 16 16" aria-hidden="true"><rect x="1" y="3" width="14" height="10" rx="1" fill="currentColor"/><path d="M1.5 3.8 8 9l6.5-5.2" fill="none" stroke="#fff" stroke-width="1.3"/></svg>
          <span>Your Address 1234<br>56, Address 789</span>
        </li>
      </ul>
    </div>
  </section>
</main>
</body>
</html>
```